Label design for Japanese healthy drink

We need new label design to give our product a new look. This is Amazake, traditional Japanese drink made out of fermented rice. This is nutrition packed drink and target audience is health conscious people. We want something simple and healthy. The attached photo is current label (for the size reference only) and food pouch the label will be attached. Please don't use anything on the label in the picture.

Target Market(s)

health conscious people (30s - 50s)

Requirements
Must have
• "Amazake"
Should not have
• too much color, picture of rice or sake

```html
<!DOCTYPE html>
<html lang="en">
<head>
<meta charset="utf-8">
<title>Amazake Label</title>
<link rel="stylesheet" href="https://fonts.googleapis.com/css2?family=Archivo:wdth,wght@125,900&family=Inter:wght@300;400&family=Noto+Sans+JP:wght@400&display=swap">
<style>
  :root {
    --ink-light: #ffffff;
    --ink-dark: #2a1a24;
    --accent: #c2185b;
    --glow-core: #cf6a5e;
    --glow-mid: #c48aa8;
    --glow-edge: #c7dcec;
    --glow-outer: #e9eef6;
  }
  html, body {
    margin: 0;
    padding: 0;
    width: 1200px;
    height: 1200px;
    overflow: hidden;
  }
  .label {
    position: relative;
    width: 1200px;
    height: 1200px;
    overflow: hidden;
    font-family: "Inter", Arial, sans-serif;
    color: var(--ink-light);
    text-align: center;
  }
  .backdrop {
    position: absolute;
    inset: 0;
    background: radial-gradient(circle 640px at 600px 560px,
      var(--glow-core) 0%,
      var(--glow-mid) 40%,
      var(--glow-edge) 75%,
      var(--glow-outer) 100%);
  }
  .kanji {
    position: absolute;
    top: 238px;
    left: 0;
    right: 0;
    font-family: "Noto Sans JP", sans-serif;
    font-size: 40px;
    letter-spacing: 2px;
  }
  .product-name {
    position: absolute;
    top: 330px;
    left: 0;
    right: 0;
    margin: 0;
    font-family: "Archivo", "Arial Black", sans-serif;
    font-weight: 900;
    font-stretch: 125%;
    font-variation-settings: "wdth" 125;
    font-size: 236px;
    line-height: 213px;
    letter-spacing: -3px;
  }
  .product-name span { display: block; }
  .tagline {
    position: absolute;
    top: 862px;
    left: 0;
    right: 0;
    margin: 0;
    font-weight: 300;
    font-size: 40px;
    line-height: 56px;
  }
  .divider {
    position: absolute;
    top: 1025px;
    left: 582px;
    width: 36px;
    height: 6px;
    background: var(--accent);
  }
  .net-weight {
    position: absolute;
    top: 1050px;
    left: 0;
    right: 0;
    font-size: 27px;
    color: var(--ink-dark);
  }
</style>
</head>
<body>
  <main class="label">
    <div class="backdrop" role="img" aria-label="Soft blurred glow of warm rose light fading into pale sky blue"></div>
    <div class="kanji" lang="ja">甘酒</div>
    <h1 class="product-name"><span>Ama</span><span>zake</span></h1>
    <p class="tagline">Traditional Japanese drink<br>made out of fermented rice</p>
    <div class="divider"></div>
    <div class="net-weight">150 g</div>
  </main>
</body>
</html>
```